Cosmetic Clinic Looking For Sign Designs

We are looking for sign design ideas for the front of our building and a lawn sign for our cosmetic injection salon.
I have uploaded the front of our building for a mock up and size, lawn posts with size and a sign that uses the same dimensions.
We would like both signs to be black for the background.

Target Market(s)

Ages 18-75

Industry/Entity Type

Beauty

Requirements
Must have
• Services we offer:
• Cosmetic Injections
• Airbrush Spray Tanning
• Eyelash Growth Serum
• Skin Care Products & More
• Everything must be on a black background
• The lawn sign must have the address: 394 Fenwick and the building sign should have the phone number.
Should not have
• Nothing can light up (no LED)
• Both signs do not need the full address. Just 394 Fenwick and the phone number

```html
<!DOCTYPE html>
<html lang="en">
<head>
<meta charset="utf-8">
<title>Bright Hour Salon – Building Sign</title>
<link rel="stylesheet" href="https://fonts.googleapis.com/css2?family=Barlow+Semi+Condensed:wght@700&display=swap">
<style>
  :root {
    --periwinkle: #7a80c0;
    --sign-black: #000000;
    --teal: #2a9fc0;
    --pink: #ee1277;
    --white: #ffffff;
    --page: #ffffff;
  }
  html, body {
    margin: 0;
    padding: 0;
    width: 1023px;
    height: 1200px;
    overflow: hidden;
    background: var(--page);
  }
  .sign {
    display: block;
    width: 1023px;
    height: 1200px;
  }
  .sign text {
    font-family: "Barlow Semi Condensed", "Arial Narrow", sans-serif;
    font-weight: 700;
  }
  .sign__frame { fill: var(--periwinkle); }
  .sign__panel { fill: var(--sign-black); }
  .strip--periwinkle { fill: var(--periwinkle); }
  .strip--pink { fill: var(--pink); }
  .strip--teal { fill: var(--teal); }
  .brand__circle { fill: var(--periwinkle); }
  .brand__name { fill: var(--teal); }
  .brand__rule { fill: var(--pink); }
  .services { fill: var(--white); letter-spacing: 1px; }
  .contact { fill: var(--pink); }
  .contact__divider { fill: var(--teal); }
</style>
</head>
<body>
<svg class="sign" viewBox="0 0 1000 1173" xmlns="http://www.w3.org/2000/svg" role="img" aria-label="Bright Hour Salon building sign">
  <!-- Frame and panel -->
  <path class="sign__frame" d="M120 243 H290 A208 208 0 0 1 702 243 H879 V1010 H120 Z"/>
  <path class="sign__panel" d="M135 258 H303.4 A193 193 0 0 1 688.6 258 H864 V993 H135 Z"/>

  <!-- Bottom colour strip -->
  <rect class="strip--periwinkle" x="120" y="993" width="187" height="17"/>
  <rect class="strip--pink" x="307" y="993" width="204" height="17"/>
  <rect class="strip--teal" x="511" y="993" width="202" height="17"/>
  <rect class="strip--periwinkle" x="713" y="993" width="166" height="17"/>

  <!-- Brand -->
  <circle class="brand__circle" cx="498" cy="274" r="125"/>
  <text class="brand__name" x="498" y="533" text-anchor="middle" font-size="118" textLength="597" lengthAdjust="spacingAndGlyphs">BRIGHT HOUR</text>
  <polygon class="brand__rule" points="192,578 372,574 372,582"/>
  <polygon class="brand__rule" points="622,574 805,578 622,582"/>
  <text class="brand__name" x="498" y="602" text-anchor="middle" font-size="64" textLength="210" lengthAdjust="spacingAndGlyphs">SALON</text>

  <!-- Services -->
  <text class="services" x="498" y="745" text-anchor="middle" font-size="72">COSMETIC</text>
  <text class="services" x="498" y="809" text-anchor="middle" font-size="72" textLength="572" lengthAdjust="spacingAndGlyphs">INJECTION SALON</text>

  <!-- Contact -->
  <text class="contact" x="433" y="907" text-anchor="end" font-size="40">394 Fenwick</text>
  <rect class="contact__divider" x="458" y="874" width="6" height="38"/>
  <text class="contact" x="489" y="907" font-size="40" textLength="273" lengthAdjust="spacingAndGlyphs">(905) 555-0147</text>
</svg>
</body>
</html>
```